Banner ads for QV that work with same theme as below banners

Love the banner ads below. Need more with attached photos. But use the same wording, font as in below banner ads. Should be QV size 1200/627 so I can use for Pictorelle and QV. Looking for great ads to use as QV ads. We do lots of ads so it will be worth your time to enter this contest you will be rewarded with a ton of work. Need several banner ads that work together. So maybe 1 of the dresses, 1 of the sweater, 1 of the leggings, 1 of the jacket

Target Market(s)

Women 24-45

Industry/Entity Type

Fashion

Requirements
Must have
• Banner ads that work for QV and Pictorelle
Nice to have
• Several options to choose from
Should not have
• not sure

```html
<!DOCTYPE html>
<html lang="en">
<head>
<meta charset="UTF-8">
<title>Our Best Sweater Ever — Shop the Look</title>
<link rel="stylesheet" href="https://fonts.googleapis.com/css2?family=Oregano:ital@1&family=Playfair+Display:wght@400;700;900&display=swap">
<style>
  :root {
    --canvas-base: #ebe5e3;
    --band-light: #f3f0ee;
    --band-mid: #efebe9;
    --ink: #2b2b2b;
    --accent: #ee7a17;
    --button-bg: #333333;
    --model-light: #d6d2dd;
    --model-mid: #bcb8cc;
    --model-dark: #8a7868;
  }
  * { margin: 0; padding: 0; box-sizing: border-box; }
  html, body {
    width: 1200px; height: 628px; overflow: hidden;
    background: var(--canvas-base);
  }
  .banner {
    position: relative;
    width: 1200px; height: 628px;
    overflow: hidden;
    background: linear-gradient(90deg, #e9e4e3 0%, #f0ebea 55%, #eeeae8 100%);
  }
  .banner__bands {
    position: absolute; inset: 0;
  }
  .banner__model {
    position: absolute;
    left: 55px; top: 0;
    width: 285px; height: 628px;
    background: linear-gradient(180deg, var(--model-dark) 0%, var(--model-mid) 22%, var(--model-light) 55%, var(--model-mid) 90%, #2a2a2e 100%);
    opacity: .85;
  }
  .headline {
    position: absolute;
    left: 760px; top: 160px;
    width: 290px;
    text-align: center;
    color: var(--ink);
    font-weight: normal;
  }
  .headline__script {
    display: block;
    font-family: 'Oregano', cursive;
    font-style: italic;
    font-size: 56px;
    line-height: 1;
    letter-spacing: 4px;
  }
  .headline__script--top { margin-left: -8px; }
  .headline__script--bottom { margin-top: 14px; margin-left: -12px; }
  .headline__product {
    display: block;
    margin-top: 10px;
    font-family: 'Playfair Display', serif;
    font-weight: 900;
    font-size: 44px;
    letter-spacing: 7px;
    margin-right: -9px;
    color: var(--accent);
    line-height: 1;
  }
  .cta {
    position: absolute;
    left: 771px; top: 369px;
    width: 269px; height: 61px;
    background: var(--button-bg);
    display: flex; align-items: center; justify-content: center;
    font-family: 'Playfair Display', serif;
    font-size: 18px;
    letter-spacing: 4px;
    color: var(--accent);
    text-decoration: none;
  }
  .cta__strong { font-weight: 900; }
  .cta__light { font-weight: 400; margin: 0 8px; }
</style>
</head>
<body>
  <main class="banner">
    <svg class="banner__bands" width="1200" height="628" viewBox="0 0 1200 628" aria-hidden="true">
      <polygon points="860,0 1200,0 1200,290 960,628 420,628" fill="var(--band-light)"/>
      <polygon points="1200,290 1200,628 960,628" fill="var(--band-mid)"/>
    </svg>

    <div class="banner__model" role="img" aria-label="Photo of a model with long wavy hair wearing an oversized lavender knit turtleneck sweater and black leggings"></div>

    <h1 class="headline">
      <span class="headline__script headline__script--top">Our Best</span>
      <span class="headline__product">SWEATER</span>
      <span class="headline__script headline__script--bottom">Ever!</span>
    </h1>

    <a class="cta" href="#">
      <span class="cta__strong">SHOP</span><span class="cta__light">THE</span><span class="cta__strong">LOOK</span>
    </a>
  </main>
</body>
</html>
```